Copper Lantern Gin

The gin is 100% proof and men and anbody 18 - 30 year old will be a target market - the bottle is very distinctive and lends itself to a square label.

The bottle is curved with a large front face that lends itself to a striking design. There should be enough space around the label to show the black gin in the bottle as this is a feature.

The current bottle with the existing label is attached below as is the new glass bottle. The new gin will be coloured black.

Font styles to use
Decorative
Script

```html
<!DOCTYPE html>
<html lang="en">
<head>
<meta charset="utf-8">
<title>Copper Lantern Gin – Label</title>
<link rel="stylesheet" href="https://fonts.googleapis.com/css2?family=Caveat+Brush&family=Oswald:wght@500;600&display=swap">
<style>
  :root {
    --page-bg: #ffffff;
    --label-black: #050505;
    --gin-red: #e5090f;
    --gin-red-deep: #6e0b0d;
    --ink-white: #ffffff;
    --script-font: "Caveat Brush", cursive;
    --caps-font: "Oswald", sans-serif;
  }

  * { box-sizing: border-box; margin: 0; padding: 0; }

  html, body {
    width: 1200px;
    height: 900px;
    overflow: hidden;
    background: var(--page-bg);
  }

  .canvas {
    position: relative;
    width: 1200px;
    height: 900px;
  }

  .label {
    position: absolute;
    left: 246px;
    top: 135px;
    width: 708px;
    height: 630px;
  }

  .label-shape {
    position: absolute;
    inset: 0;
    width: 100%;
    height: 100%;
  }

  .label-strength {
    position: absolute;
    top: 46px;
    left: 0;
    width: 100%;
    text-align: center;
    font-family: var(--caps-font);
    font-weight: 500;
    font-size: 25px;
    letter-spacing: 9px;
    color: var(--gin-red);
  }

  .label-band {
    position: absolute;
    top: 99px;
    left: 34px;
    right: 34px;
    height: 30px;
    background: linear-gradient(90deg, var(--gin-red-deep) 0%, var(--gin-red) 55%, var(--gin-red) 100%);
  }

  .label-type {
    position: absolute;
    top: 0;
    left: 50%;
    transform: translateX(-50%);
    width: 214px;
    height: 30px;
    line-height: 30px;
    text-align: center;
    background: #c8070c;
    font-family: var(--caps-font);
    font-weight: 600;
    font-size: 21px;
    letter-spacing: 3px;
    color: var(--ink-white);
  }

  .label-illustration {
    position: absolute;
    top: 205px;
    left: 80px;
    width: 540px;
    height: 225px;
    border-radius: 40px;
    background: radial-gradient(ellipse at 55% 55%, rgba(210, 16, 20, 0.85) 0%, rgba(150, 10, 14, 0.55) 45%, rgba(5, 5, 5, 0) 75%);
  }

  .label-name {
    position: absolute;
    left: 0;
    width: 100%;
    text-align: center;
    font-family: var(--script-font);
    font-size: 108px;
    line-height: 1;
    color: var(--ink-white);
  }

  .label-name--top { top: 135px; }
  .label-name--bottom { top: 405px; }

  .label-detail {
    position: absolute;
    top: 500px;
    font-family: var(--caps-font);
    font-weight: 600;
    font-size: 19px;
    letter-spacing: 1px;
    color: var(--ink-white);
  }

  .label-detail--volume { left: 64px; }
  .label-detail--abv { right: 64px; }
</style>
</head>
<body>
  <main class="canvas">
    <section class="label">
      <svg class="label-shape" viewBox="0 0 708 630" aria-hidden="true">
        <defs>
          <linearGradient id="label-border" x1="0" y1="0" x2="1" y2="0">
            <stop offset="0" stop-color="#a00a0e"/>
            <stop offset="0.5" stop-color="#e5090f"/>
            <stop offset="1" stop-color="#f2131a"/>
          </linearGradient>
        </defs>
        <path d="M150 58 Q354 6 558 58 L690 160 Q682 340 672 498 L482 610 Q354 636 226 610 L36 498 Q26 340 18 160 Z"
              fill="#050505" stroke="url(#label-border)" stroke-width="10" stroke-linejoin="round"/>
      </svg>

      <p class="label-strength">NAVY STRENGH</p>

      <div class="label-band">
        <p class="label-type">BRITISH GIN</p>
      </div>

      <div class="label-illustration" role="img" aria-label="Red tribal-style wolf illustration prowling across the label"></div>

      <h1 class="label-name label-name--top">Copper</h1>
      <h1 class="label-name label-name--bottom">Lantern</h1>

      <p class="label-detail label-detail--volume">50CL</p>
      <p class="label-detail label-detail--abv">57%ABV</p>
    </section>
  </main>
</body>
</html>
```